creative design for a downloadable PDF

I have a PDF document that needs some creative inspiration on two pages. This PDF will be available for download from our website and contains information on a new service offering. The general design elements are finished and will not be altered: the cover page, headers/footers, color scheme, and back page are all fixed. We just have a 'Table of Contents' page and a 'Workflow' page that are uninteresting and lack inspiration. The Workflow page in particular is concerning as it fails to convey our step-by-step approach to project management and how our customers progress through the steps over time. We had a simple bulleted list (see the MS Word Doc), then went to 'tiles' which zigzag across the page (see the PDF). Anyway we need someone to display this in a more thoughtful and easily understood way.

```html
<!DOCTYPE html>
<html lang="en">
<head>
<meta charset="utf-8">
<title>The CREST Purchasing Experience – Our Work Flow</title>
<link rel="stylesheet" href="https://fonts.googleapis.com/css2?family=Roboto:wght@400;500;700;900&display=swap">
<style>
  :root {
    --page-bg: #e8fdfd;
    --band-dark: #1f74b9;
    --band-light: #2c97db;
    --ribbon: #1d6aa0;
    --cyan: #05f5f8;
    --orange: #ff7f00;
    --purple: #7209ee;
    --red: #ff0000;
    --white: #ffffff;
  }
  * { box-sizing: border-box; margin: 0; padding: 0; }
  html, body { width: 928px; height: 1200px; overflow: hidden; }
  body {
    position: relative;
    background: var(--page-bg);
    font-family: "Roboto", Arial, sans-serif;
    color: var(--white);
  }
  .page-header, .page-footer {
    position: absolute; left: 0; width: 928px;
    background: linear-gradient(90deg, var(--band-dark), var(--band-light));
  }
  .page-header { top: 0; height: 80px; }
  .page-footer { top: 1149px; height: 51px; display: flex; align-items: center; justify-content: center; gap: 10px; font-size: 15.5px; font-weight: 500; }
  .doc-title { position: absolute; left: 82px; top: 34px; font-size: 13.5px; font-weight: 500; }
  .page-number { position: absolute; left: 837px; top: 34px; font-size: 13.5px; font-weight: 500; }

  .section-title {
    position: absolute; left: 0; top: 81px; width: 269px; height: 115px;
    background: var(--red); border-radius: 0 0 34px 0;
    padding: 16px 0 0 33px; font-weight: 900; line-height: 1;
  }
  .section-title .big { display: block; font-size: 44px; letter-spacing: 1px; }
  .section-title .small { display: block; font-size: 28px; margin-top: 4px; }
  .section-title svg { position: absolute; left: 209px; top: 22px; }

  .ready-ribbon { position: absolute; left: 846px; top: 126px; }
  .ready-text {
    position: absolute; left: 887px; top: 610px;
    transform: translate(-50%, -50%) rotate(-90deg);
    white-space: nowrap; font-size: 24.5px; font-weight: 700; letter-spacing: 0.2px;
  }

  .step {
    position: absolute; border-radius: 33px; padding: 0 8px 0 17px;
  }
  .step.cyan { background: var(--cyan); left: 26px; width: 226px; padding-left: 9px; }
  .step.orange { background: var(--orange); }
  .step.purple { background: var(--purple); }
  .step.red { background: var(--red); }
  .col-2 { left: 283px; width: 227px; }
  .col-3 { left: 531px; width: 227px; }

  .step-number {
    position: absolute; right: 20px; top: 16px; width: 30px; height: 30px;
    border: 2.5px solid var(--white); border-radius: 50%;
    display: flex; align-items: center; justify-content: center;
    font-size: 12.5px; font-weight: 700;
  }
  .cyan .step-number { background: rgba(255,255,255,0.35); right: 19px; }
  .step-icon { position: absolute; left: 17px; top: 16px; }
  .cyan .step-icon { left: 10px; }
  .step-text { position: absolute; top: 63px; left: 17px; right: 8px; font-size: 14.6px; line-height: 16.5px; }
  .cyan .step-text { left: 9px; }
  .red .step-text { font-size: 12.4px; line-height: 14.6px; left: 13px; }
  .step-notes { list-style: none; margin-top: 17px; font-size: 12px; line-height: 14.6px; }
  .step-notes li { position: relative; padding-left: 17px; margin-bottom: 10px; }
  .step-notes li::before {
    content: ""; position: absolute; left: 2px; top: 2px; width: 7px; height: 7px;
    border: 1.6px solid var(--white); border-radius: 50%;
  }
</style>
</head>
<body>
  <header class="page-header">
    <span class="doc-title">The CREST Purchasing Experience</span>
    <span class="page-number">3</span>
  </header>

  <div class="section-title">
    <span class="big">OUR</span>
    <span class="small">WORK FLOW</span>
    <svg width="50" height="50" viewBox="0 0 50 50" aria-hidden="true">
      <circle cx="25" cy="25" r="22" fill="none" stroke="#fff" stroke-width="4"/>
      <path d="M18 19 l7 6 l7 -6 M18 27 l7 6 l7 -6" fill="none" stroke="#fff" stroke-width="3.5" stroke-linecap="round" stroke-linejoin="round"/>
    </svg>
  </div>

  <svg class="ready-ribbon" width="82" height="974" viewBox="0 0 82 974" aria-hidden="true">
    <path d="M82 0 L16 60 Q0 75 0 100 L0 874 Q0 899 16 914 L82 974 Z" fill="var(--ribbon)"/>
  </svg>
  <div class="ready-text">IF YOU ARE READY,&nbsp; TIS TAKES AS ;ITTL;E AS THREE WEEKS</div>

  <!-- Column 1 -->
  <section class="step cyan" style="top:214px;height:179px">
    <span class="step-number">01</span>
    <p class="step-text" style="top:76px">Medical Device Original Equip-ment Manufacturer (OEM) creates account on the Heron Medical (HMPS) web portal</p>
  </section>

  <section class="step cyan" style="top:400px;height:276px">
    <span class="step-number">02</span>
    <div class="step-text" style="top:70px">
      <p>OEM digitally signs ‘readiness checklist’ to gain access to downloadables</p>
      <ul class="step-notes">
        <li>The readiness checklist protects the OEM’s investment by confirming critical bench-marks, AND</li>
        <li>Necessary data and delivera-bles to HMPS are immediately available</li>
      </ul>
    </div>
  </section>

  <section class="step cyan" style="top:683px;height:132px">
    <svg class="step-icon" width="42" height="42" viewBox="0 0 42 42" aria-hidden="true" fill="none" stroke="#fff" stroke-width="1.8">
      <rect x="2" y="4" width="26" height="34" rx="2"/><rect x="12" y="8" width="28" height="22" rx="2"/>
      <path d="M16 14h20M16 19h20M16 24h14"/>
    </svg>
    <span class="step-number">03</span>
    <p class="step-text">OEM downloads eBook #3, Mutual NDA, and CREST contract</p>
  </section>

  <section class="step cyan" style="top:823px;height:112px">
    <svg class="step-icon" width="40" height="40" viewBox="0 0 40 40" aria-hidden="true" fill="none" stroke="#fff" stroke-width="1.8">
      <circle cx="20" cy="20" r="10"/><path d="M20 13v14M24 16h-6a2 2 0 0 0 0 4h4a2 2 0 0 1 0 4h-6"/>
      <path d="M2 36h10l8-4M38 4h-10l-8 4"/>
    </svg>
    <span class="step-number">04</span>
    <p class="step-text">HMPS/OEM sign mutual NDA</p>
  </section>

  <section class="step orange" style="left:26px;width:227px;top:943px;height:172px;padding-left:9px">
    <svg class="step-icon" style="left:9px" width="42" height="44" viewBox="0 0 42 44" aria-hidden="true" fill="none" stroke="#fff" stroke-width="1.8">
      <path d="M4 2h18l8 8v12M4 2v36h16"/><path d="M9 16h14M9 22h10M9 28h8"/>
      <circle cx="30" cy="32" r="10"/><path d="M30 38v-12M25 30l5-5 5 5"/>
    </svg>
    <span class="step-number">05</span>
    <p class="step-text" style="left:9px;top:66px">OEM uploads critical info such as their top-level assembly drawing (released data only) for evaluation</p>
  </section>

  <!-- Column 2 -->
  <section class="step orange col-2" style="top:91px;height:160px">
    <svg class="step-icon" width="40" height="40" viewBox="0 0 40 40" aria-hidden="true" fill="none" stroke="#fff" stroke-width="1.8">
      <rect x="2" y="2" width="36" height="36" rx="3"/><path d="M2 30h36M6 18h6l3-6 5 12 3-6h11"/>
    </svg>
    <span class="step-number">06</span>
    <p class="step-text">HMPS evaluates drawing and verifies that CREST is a viable solution for the specific medical device configuration</p>
  </section>

  <section class="step orange col-2" style="top:256px;height:162px">
    <svg class="step-icon" width="34" height="42" viewBox="0 0 34 42" aria-hidden="true" fill="none" stroke="#fff" stroke-width="1.8">
      <rect x="4" y="2" width="18" height="30" rx="2"/><path d="M10 8v10M14 8v10M20 20l10 10v10H16l-6-8"/>
    </svg>
    <span class="step-number">07</span>
    <p class="step-text">HMPS sends quote for CREST routine production to 10K units/yr. pricing, along with credit terms</p>
  </section>

  <section class="step orange col-2" style="top:423px;height:152px">
    <svg class="step-icon" width="44" height="42" viewBox="0 0 44 42" aria-hidden="true" fill="none" stroke="#fff" stroke-width="1.8">
      <rect x="2" y="2" width="40" height="38" rx="2"/><path d="M2 9h40M6 16h10M6 22h6"/>
      <circle cx="24" cy="30" r="6"/><circle cx="24" cy="30" r="2"/>
    </svg>
    <span class="step-number">08</span>
    <p class="step-text">OEM submits $5K nonrefund-able deposit, which is fully creditable to CREST or custom development project</p>
  </section>

  <section class="step orange col-2" style="top:580px;height:156px">
    <svg class="step-icon" width="42" height="44" viewBox="0 0 42 44" aria-hidden="true" fill="none" stroke="#fff" stroke-width="1.8">
      <path d="M8 18a8 8 0 0 1 4-14 10 10 0 0 1 18 4 6 6 0 0 1 4 10z"/>
      <rect x="14" y="22" width="14" height="14" rx="1"/><path d="M18 26v-2a3 3 0 0 1 6 0v2M21 36v6"/>
    </svg>
    <span class="step-number">09</span>
    <p class="step-text">OEM downloads DocVault; allowing 24-hour access to restricted doc set to verify contents</p>
  </section>

  <section class="step orange col-2" style="top:741px;height:140px">
    <svg class="step-icon" width="48" height="40" viewBox="0 0 48 40" aria-hidden="true" fill="none" stroke="#fff" stroke-width="1.8">
      <rect x="2" y="2" width="44" height="32" rx="2"/><rect x="12" y="6" width="22" height="8" rx="1"/>
      <path d="M8 20h20M8 26h16"/><circle cx="36" cy="28" r="5"/>
    </svg>
    <span class="step-number">10</span>
    <p class="step-text">OEM provided with FDA Master File number; allowed time to verify MF on fda.gov</p>
  </section>

  <section class="step orange col-2" style="top:886px;height:120px">
    <svg class="step-icon" width="40" height="40" viewBox="0 0 40 40" aria-hidden="true" fill="none" stroke="#fff" stroke-width="1.8">
      <rect x="6" y="2" width="30" height="36" rx="2"/><path d="M2 10h8M2 20h8M2 30h8"/>
      <circle cx="21" cy="16" r="4"/><path d="M13 30a8 8 0 0 1 16 0z"/>
    </svg>
    <span class="step-number">11</span>
    <p class="step-text">OEM and HMPS formalize and sign the CREST contract</p>
  </section>

  <section class="step purple col-2" style="top:1013px;height:121px">
    <svg class="step-icon" width="34" height="44" viewBox="0 0 34 44" aria-hidden="true" fill="none" stroke="#fff" stroke-width="1.8">
      <circle cx="17" cy="9" r="7"/><path d="M14 6v6M17 12V6h3a2 2 0 0 1 0 3h-3M17 16v6"/>
      <rect x="2" y="24" width="30" height="8"/><rect x="2" y="34" width="30" height="8"/>
    </svg>
    <span class="step-number">12</span>
    <p class="step-text">OEM and HMPS sign the IP Escrow contract</p>
  </section>

  <!-- Column 3 -->
  <section class="step purple col-3" style="top:91px;height:140px">
    <svg class="step-icon" width="36" height="42" viewBox="0 0 36 42" aria-hidden="true" fill="none" stroke="#fff" stroke-width="2">
      <path d="M18 2l15 6v12c0 10-7 17-15 20C10 37 3 30 3 20V8z"/><path d="M11 21l5 5 10-10"/>
    </svg>
    <span class="step-number">13</span>
    <p class="step-text">HMPS uploads document set to the Escrow portal with speci-fied security controls</p>
  </section>

  <section class="step purple col-3" style="top:235px;height:125px">
    <svg class="step-icon" width="46" height="42" viewBox="0 0 46 42" aria-hidden="true" fill="none" stroke="#fff" stroke-width="1.8">
      <circle cx="26" cy="10" r="8"/><path d="M28 6h-3a2 2 0 0 0 0 4h2a2 2 0 0 1 0 4h-3"/>
      <path d="M2 32l8-8h10l4 4h-8M14 28h14l14-8a2 2 0 0 1 2 4L28 36H12l-4 4"/>
    </svg>
    <span class="step-number">14</span>
    <p class="step-text">OEM transfers payment balance to Escrow</p>
  </section>

  <section class="step purple col-3" style="top:365px;height:124px">
    <svg class="step-icon" width="46" height="46" viewBox="0 0 46 46" aria-hidden="true" fill="none" stroke="#fff" stroke-width="1.8">
      <circle cx="23" cy="4" r="3"/><circle cx="23" cy="20" r="6"/><path d="M23 16v8"/>
      <circle cx="10" cy="34" r="4"/><path d="M2 46v-2a8 8 0 0 1 16 0v2z"/>
      <circle cx="36" cy="34" r="4"/><path d="M28 46v-2a8 8 0 0 1 16 0v2z"/>
      <path d="M6 18v-6h6M40 18v-6h-6"/>
    </svg>
    <span class="step-number">15</span>
    <p class="step-text" style="top:74px">Escrow agent verifies receipt of both IP and funds</p>
  </section>

  <section class="step purple col-3" style="top:495px;height:158px">
    <svg class="step-icon" width="46" height="46" viewBox="0 0 46 46" aria-hidden="true" fill="none" stroke="#fff" stroke-width="1.8">
      <rect x="8" y="2" width="30" height="40"/><path d="M2 44h42"/>
      <rect x="16" y="14" width="12" height="10" rx="1"/><path d="M19 14v-3a3 3 0 0 1 6 0v3M24 30v10h10"/>
    </svg>
    <span class="step-number">16</span>
    <p class="step-text" style="top:70px">OEM given short term, unrestrict-ed access to the document set to verify contents and accessibil-ity</p>
  </section>

  <section class="step purple col-3" style="top:659px;height:161px">
    <svg class="step-icon" width="46" height="44" viewBox="0 0 46 44" aria-hidden="true" fill="none" stroke="#fff" stroke-width="1.8">
      <rect x="2" y="2" width="14" height="10" rx="1"/><circle cx="34" cy="6" r="4"/>
      <rect x="24" y="16" width="20" height="26"/><circle cx="8" cy="32" r="3"/><circle cx="17" cy="32" r="3"/>
      <path d="M2 42a6 6 0 0 1 12 0M11 42a6 6 0 0 1 12 0"/>
    </svg>
    <span class="step-number">17</span>
    <p class="step-text" style="top:70px">OEM and HMPS mutually green-light the transaction via secure conference call with escrow agent</p>
  </section>

  <section class="step purple col-3" style="top:827px;height:118px">
    <svg class="step-icon" width="44" height="46" viewBox="0 0 44 46" aria-hidden="true" fill="none" stroke="#fff" stroke-width="1.8">
      <circle cx="22" cy="20" r="18"/><path d="M4 20h36M22 2c-8 8-8 28 0 36M22 2c8 8 8 28 0 36"/>
      <path d="M8 44v-8h28v8"/>
    </svg>
    <span class="step-number">18</span>
    <p class="step-text">Escrow agent releases funds and IP to respective parties</p>
  </section>

  <section class="step red col-3" style="top:951px;height:139px;left:530px">
    <svg class="step-icon" style="left:13px" width="48" height="50" viewBox="0 0 48 50" aria-hidden="true" fill="none" stroke="#fff" stroke-width="1.8">
      <path d="M24 4a21 21 0 1 0 0 42"/><path d="M24 12a13 13 0 1 0 0 26"/>
      <path d="M24 8h10l4-4M24 18h16M24 25h20M24 32h16M24 42h10l4 4"/>
      <circle cx="40" cy="4" r="2"/><circle cx="42" cy="18" r="2"/><circle cx="46" cy="25" r="2"/><circle cx="42" cy="32" r="2"/><circle cx="40" cy="46" r="2"/>
    </svg>
    <span class="step-number">19</span>
    <p class="step-text" style="top:61px">Onus on OEM to complete engineering rationale for adoption with support from HMPS</p>
  </section>

  <footer class="page-footer">
    <span>www.heronmed.example</span><span>•</span><span>info@heronmed.example</span><span>&nbsp;•</span><span>555-014-2290</span>
  </footer>
</body>
</html>
```